Harlow Ridge Partners Business Cards

Design Business cards in a format where I can change the information and utilize a third party buisness card printing company

Contact Information for Business Card

Want Logo and Name on Back. Looking for Spot UV style shine on Logo. Probably Black background. Want smaller logo on front with contact details. Like rounded edges or something else interesting.

Requirements
Must have
• Strong masculine look.

```html
<!DOCTYPE html>
<html lang="en">
<head>
<meta charset="utf-8">
<title>Harlow Ridge Partners Business Cards</title>
<link rel="stylesheet" href="https://fonts.googleapis.com/css2?family=Cinzel:wght@400;600&family=Arimo:wght@400&display=swap">
<style>
  :root {
    --canvas: #2b2623;
    --card: #0d0d0d;
    --card-edge: #1a1a1a;
    --gloss: #3a3a3a;
    --gloss-light: #5c5c5c;
    --silver: #d9d9d9;
    --silver-dim: #9a9a9a;
    --rule: #555555;
  }
  * { margin: 0; padding: 0; box-sizing: border-box; }
  html, body { width: 1200px; height: 780px; overflow: hidden; }
  body {
    background: var(--canvas);
    display: flex;
    align-items: center;
    justify-content: center;
    gap: 60px;
  }
  .card {
    width: 520px;
    height: 300px;
    background: var(--card);
    border: 1px solid var(--card-edge);
    border-radius: 10px;
    box-shadow: 0 18px 40px rgba(0,0,0,0.55);
    position: relative;
  }

  /* Back: brand name only */
  .card-back {
    display: flex;
    flex-direction: column;
    align-items: center;
    justify-content: center;
  }
  .brand-square {
    width: 54px;
    height: 54px;
    background: var(--gloss);
    margin-bottom: 26px;
  }
  .brand-name {
    font-family: "Cinzel", serif;
    font-weight: 600;
    font-size: 34px;
    letter-spacing: 1px;
    color: var(--gloss-light);
  }
  .brand-sub {
    font-family: "Cinzel", serif;
    font-weight: 600;
    font-size: 13px;
    letter-spacing: 14px;
    color: var(--gloss-light);
    margin-top: 6px;
    padding-left: 14px;
  }

  /* Front: contact details */
  .card-front {
    display: flex;
    align-items: center;
    padding: 0 36px;
  }
  .front-brand {
    width: 170px;
    display: flex;
    flex-direction: column;
    align-items: center;
    gap: 14px;
  }
  .front-brand .brand-square { width: 70px; height: 70px; margin: 0; }
  .front-brand-name {
    font-family: "Cinzel", serif;
    font-weight: 600;
    font-size: 14px;
    letter-spacing: 1px;
    color: var(--gloss-light);
    text-align: center;
    line-height: 1.3;
  }
  .divider {
    width: 1px;
    height: 170px;
    background: var(--rule);
    margin: 0 26px;
  }
  .contact { color: var(--silver); }
  .person-name {
    font-family: "Cinzel", serif;
    font-weight: 600;
    font-size: 17px;
    letter-spacing: 1px;
    color: var(--gloss-light);
  }
  .person-title {
    font-family: "Cinzel", serif;
    font-size: 11px;
    letter-spacing: 1px;
    color: var(--silver-dim);
    margin-bottom: 12px;
  }
  .contact-line {
    font-family: "Arimo", sans-serif;
    font-size: 14px;
    line-height: 1.45;
    display: flex;
    align-items: center;
    gap: 8px;
  }
  .contact-line svg { width: 12px; height: 12px; fill: var(--silver-dim); }
</style>
</head>
<body>
  <section class="card card-back">
    <div class="brand-square"></div>
    <div class="brand-name">HARLOW RIDGE</div>
    <div class="brand-sub">PARTNERS</div>
  </section>

  <section class="card card-front">
    <div class="front-brand">
      <div class="brand-square"></div>
      <div class="front-brand-name">HARLOW RIDGE<br>PARTNERS</div>
    </div>
    <div class="divider"></div>
    <div class="contact">
      <div class="person-name">MARCUS HALE</div>
      <div class="person-title">MANAGING DIRECTOR</div>
      <div class="contact-line">#214 88 N Ridgeline Street</div>
      <div class="contact-line">Kingsford Canada</div>
      <div class="contact-line">
        <svg viewBox="0 0 24 24" aria-hidden="true"><path d="M6.6 10.8a15.1 15.1 0 0 0 6.6 6.6l2.2-2.2a1 1 0 0 1 1-.25 11.4 11.4 0 0 0 3.6.57 1 1 0 0 1 1 1V20a1 1 0 0 1-1 1A17 17 0 0 1 3 4a1 1 0 0 1 1-1h3.5a1 1 0 0 1 1 1c0 1.25.2 2.45.57 3.57a1 1 0 0 1-.25 1z"/></svg>
        028-555-0192
      </div>
      <div class="contact-line">
        <svg viewBox="0 0 24 24" aria-hidden="true"><path d="M2 5h20v14H2z M2 5l10 8 10-8" fill="none" stroke="#9a9a9a" stroke-width="2"/></svg>
        marcushale@harlowridge.com
      </div>
    </div>
  </section>
</body>
</html>
```